Stationary/business card/envelope design for Larkvale Dentalcare

We are located in the foothills of the sierra nevada mountains. We are looking for a beautiful classy modern stationary. We need evelopes and business card design all to flow seamlessly. Envelope design.

Additional office address 4816 Meridian Wy., Suite B, Fernhill, OR 97999 Phone: pending Fax: pending.

3 different Drs on each business card:
Helen R. Marsh, DDS
Orla P. Marsh, DDS
Rebecca S. Halvey, DDS

Target Market(s)

Dental patients

Industry/Entity Type

Dental

Contact Information for Business Card

Two sided. See example.

Font styles to use
Sans Serif

Requirements
Must have
• One sided business cards. Need envelope design.
Colors should match existing logo.

Helen R. Marsh, DDS
Orla P. Marsh, DDS
Rebecca S. Halvey, DDS

```html
<!DOCTYPE html>
<html lang="en">
<head>
<meta charset="utf-8">
<title>Larkvale Dentalcare – Business Cards</title>
<link rel="stylesheet" href="https://fonts.googleapis.com/css2?family=Lato:wght@400;700;900&display=swap">
<style>
  :root {
    --green: #1c6a34;
    --blue: #2aa4d2;
    --ink: #4f5358;
    --rule: #8a8d90;
    --paper: #fbfbfa;
    --backdrop: #e4e4e2;
  }
  * { box-sizing: border-box; margin: 0; padding: 0; }
  html, body { width: 1200px; height: 900px; overflow: hidden; }
  body {
    background: var(--backdrop);
    font-family: "Lato", sans-serif;
    color: var(--ink);
    display: flex;
    align-items: center;
    justify-content: center;
    gap: 40px;
  }
  .card {
    position: relative;
    width: 540px;
    height: 309px;
    background: var(--paper);
    box-shadow: 0 10px 28px rgba(0,0,0,.14);
    overflow: hidden;
  }
  .brand {
    position: absolute;
    display: flex;
    align-items: center;
    gap: 8px;
  }
  .brand-dot {
    width: 34px; height: 34px;
    border-radius: 50%;
    background: var(--blue);
  }
  .brand-name {
    font-weight: 700;
    font-size: 17px;
    color: var(--green);
    line-height: 1.05;
    width: 90px;
  }
  .doctor-name {
    font-weight: 900;
    color: var(--green);
    font-size: 22px;
    letter-spacing: -.2px;
  }
  .doctor-title { font-size: 14px; color: var(--ink); }

  /* Appointment card */
  .appt .brand { left: 26px; top: 30px; }
  .appt .contact-lines {
    position: absolute; right: 30px; top: 24px;
    text-align: right; font-size: 11.5px; line-height: 1.45;
  }
  .appt .contact-lines span { color: var(--blue); }
  .appt .identity { position: absolute; right: 30px; top: 72px; text-align: right; }
  .appt .divider {
    position: absolute; left: 26px; right: 30px; top: 140px;
    border-top: 1px solid var(--rule);
  }
  .appt .next-label {
    position: absolute; left: 26px; top: 156px;
    color: var(--blue); font-size: 16px; letter-spacing: .4px;
  }
  .days {
    position: absolute; left: 206px; top: 157px;
    display: flex; gap: 14px; font-size: 13px; letter-spacing: .6px;
  }
  .day { display: flex; align-items: center; gap: 5px; }
  .day::before {
    content: ""; width: 9px; height: 9px; border-radius: 50%;
    border: 1.3px solid var(--blue);
  }
  .fill-row {
    position: absolute; left: 206px; right: 30px;
    display: flex; align-items: flex-end; gap: 8px;
    color: var(--blue); font-size: 15px;
  }
  .fill-row .blank { flex: 1; border-bottom: 1px solid var(--rule); height: 14px; }
  .fill-row.date { top: 188px; }
  .fill-row.time { top: 216px; }
  .notice-band {
    position: absolute; left: 0; right: 0; bottom: 0; height: 44px;
    background: var(--blue); color: #fff;
    display: flex; align-items: center; justify-content: center;
    font-size: 11.5px; letter-spacing: 2.6px; text-transform: uppercase;
  }

  /* Contact card */
  .contact .brand { right: 26px; top: 30px; }
  .contact .identity { position: absolute; left: 30px; top: 170px; }
  .contact .doctor-name { font-size: 24px; }
  .contact .doctor-title { font-size: 15px; }
  .contact .divider {
    position: absolute; left: 30px; right: 30px; top: 228px;
    border-top: 1.3px solid var(--green);
  }
  .details {
    position: absolute; left: 30px; right: 30px; top: 237px;
    display: flex; font-size: 11.5px; line-height: 1.6;
  }
  .details .group { padding: 0 12px; border-left: 1px solid var(--green); }
  .details .group:first-child { padding-left: 0; border-left: none; }
  .details .item { display: flex; align-items: center; gap: 6px; }
  .details svg { width: 11px; height: 11px; fill: var(--blue); flex: none; }
  .edge-band { position: absolute; left: 0; bottom: 0; width: 540px; height: 14px; }
</style>
</head>
<body>

<section class="card appt" aria-label="Appointment card">
  <div class="brand">
    <div class="brand-dot"></div>
    <div class="brand-name">Larkvale Dentalcare</div>
  </div>
  <div class="contact-lines">
    <div><span>Office:</span> (555) 555-0142</div>
    <div><span>Fax:</span> (555) 555-0178</div>
  </div>
  <div class="identity">
    <div class="doctor-name">Helen R. Marsh, DDS</div>
    <div class="doctor-title">President &amp; CEO</div>
  </div>
  <div class="divider"></div>
  <div class="next-label">NEXT APPOINTMENT:</div>
  <div class="days">
    <span class="day">Mon</span><span class="day">Tue</span><span class="day">Wed</span><span class="day">Thur</span><span class="day">Fri</span>
  </div>
  <div class="fill-row date">Date:<span class="blank"></span></div>
  <div class="fill-row time">Time:<span class="blank"></span></div>
  <div class="notice-band">If unable to keep appointment, kindly give 24 hour notice</div>
</section>

<section class="card contact" aria-label="Contact card">
  <div class="brand">
    <div class="brand-dot"></div>
    <div class="brand-name">Larkvale Dentalcare</div>
  </div>
  <div class="identity">
    <div class="doctor-name">Helen R. Marsh, DDS</div>
    <div class="doctor-title">President &amp; CEO</div>
  </div>
  <div class="divider"></div>
  <div class="details">
    <div class="group">
      <div class="item"><svg viewBox="0 0 24 24"><path d="M6.6 10.8a15 15 0 0 0 6.6 6.6l2.2-2.2c.3-.3.7-.4 1-.2 1.1.4 2.3.6 3.6.6.6 0 1 .4 1 1V20c0 .6-.4 1-1 1A17 17 0 0 1 3 4c0-.6.4-1 1-1h3.5c.6 0 1 .4 1 1 0 1.3.2 2.5.6 3.6.1.3 0 .7-.2 1z"/></svg>555-555-0142</div>
      <div class="item"><svg viewBox="0 0 24 24"><path d="M7 3h10v5H7zM4 9h16a2 2 0 0 1 2 2v6h-4v4H6v-4H2v-6a2 2 0 0 1 2-2zm4 7v3h8v-3z"/></svg>555-555-0178</div>
    </div>
    <div class="group">
      <div class="item"><svg viewBox="0 0 24 24"><path d="M2 5h20v14H2zm2 2v.5l8 5 8-5V7l-8 5z"/></svg>larkvaledentalcare@mail.com</div>
      <div class="item"><svg viewBox="0 0 24 24"><path d="M12 2a10 10 0 1 0 0 20 10 10 0 0 0 0-20zm6.9 9h-3a15 15 0 0 0-1.3-5.7A8 8 0 0 1 18.9 11zM12 4c1 1.3 1.8 4 1.9 7h-3.8C10.2 8 11 5.3 12 4zM9.4 5.3A15 15 0 0 0 8.1 11h-3a8 8 0 0 1 4.3-5.7zM5.1 13h3a15 15 0 0 0 1.3 5.7A8 8 0 0 1 5.1 13zM12 20c-1-1.3-1.8-4-1.9-7h3.8c-.1 3-.9 5.7-1.9 7zm2.6-1.3a15 15 0 0 0 1.3-5.7h3a8 8 0 0 1-4.3 5.7z"/></svg>www.larkvaledentalcare.com</div>
    </div>
    <div class="group">
      <div>4816 Meridian Wy.,</div>
      <div>Suite B, Fernhill, OR 97999</div>
    </div>
  </div>
  <svg class="edge-band" viewBox="0 0 540 14" preserveAspectRatio="none" aria-hidden="true">
    <polygon points="0,6 470,6 476,0 540,0 540,14 0,14" fill="var(--blue)"/>
    <polygon points="480,0 540,0 540,14 472,14" fill="var(--green)"/>
  </svg>
</section>

</body>
</html>
```